Business Card and Word .doc header and footer required

I need a business card designed for my cybersecurity consulting company. Also required, is a header and footer to be ued for my word documents.
Attached is the Logo design, font and rgb used.

Industry/Entity Type

Cyber Security Consulting

Contact Information for Business Card

Name, Phone, email, website

Colors
0054AA
0677BA
7BADD7
CADEEF
E8F1F8

Requirements
Must have
• Sleek, modern

```html
<!DOCTYPE html>
<html lang="en">
<head>
<meta charset="utf-8">
<title>Harlow Bay Consulting – Stationery</title>
<link rel="stylesheet" href="https://fonts.googleapis.com/css2?family=Montserrat:wght@300;400;500;600;700&display=swap">
<style>
  :root {
    --navy: #17213d;
    --blue: #1a72a4;
    --sky: #2a9fc9;
    --ink: #1d4f86;
    --grey: #5b5f66;
    --paper: #ffffff;
    --backdrop: #f3f4f6;
    --faint: #eeeeee;
  }
  * { margin: 0; padding: 0; box-sizing: border-box; }
  html, body { width: 855px; height: 1200px; overflow: hidden; }
  body { background: var(--backdrop); font-family: "Montserrat", sans-serif; position: relative; }

  .stage { position: absolute; left: 38px; top: 259px; width: 951px; height: 832px; transform: scale(0.82); transform-origin: 0 0; }

  /* Letterhead */
  .letterhead { position: absolute; left: 0; top: 0; width: 589px; height: 832px; background: var(--paper); box-shadow: 0 2px 8px rgba(0,0,0,.12); overflow: hidden; }
  .letterhead__header, .letterhead__footer { position: absolute; left: 0; width: 589px; }
  .letterhead__header { top: 0; height: 150px; }
  .letterhead__footer { bottom: 0; height: 60px; }
  .brand { position: absolute; display: flex; align-items: center; gap: 10px; }
  .brand__dot { border-radius: 50%; border: 3px solid var(--sky); flex: none; }
  .brand__name { font-weight: 600; color: #e4e8ee; white-space: nowrap; letter-spacing: .5px; }
  .letterhead .brand { left: 26px; top: 44px; }
  .letterhead .brand__dot { width: 66px; height: 66px; }
  .letterhead .brand__name { font-size: 21px; }

  .header-contacts { position: absolute; left: 438px; top: 28px; list-style: none; color: #fff; font-size: 7px; font-weight: 500; }
  .header-contacts li { display: flex; align-items: flex-start; gap: 10px; margin-bottom: 10px; line-height: 9px; }
  .header-contacts svg { width: 10px; height: 10px; flex: none; }

  .subject { position: absolute; left: 72px; top: 258px; font-size: 23px; font-weight: 300; color: var(--sky); }
  .date { position: absolute; right: 81px; top: 268px; font-size: 10px; color: var(--grey); font-weight: 500; }
  .letter-body { position: absolute; left: 74px; top: 311px; width: 434px; font-size: 10.3px; line-height: 12.8px; color: var(--grey); }
  .letter-body p { margin-bottom: 25px; }
  .signature { position: absolute; left: 402px; top: 620px; width: 66px; height: 60px; background: linear-gradient(135deg, #e6e9f2, #cfd5e6); border-radius: 4px; }
  .signatory { position: absolute; left: 360px; top: 688px; width: 150px; text-align: center; }
  .signatory__name { font-size: 13px; font-weight: 700; color: #222; }
  .signatory__role { font-size: 11px; font-weight: 500; color: var(--sky); margin-top: 2px; }

  /* Business cards */
  .card { position: absolute; left: 552px; width: 399px; height: 228px; background: var(--paper); box-shadow: 0 2px 8px rgba(0,0,0,.18); overflow: hidden; }
  .card--front { top: 171px; }
  .card--back { top: 435px; }
  .card__panel { position: absolute; left: 90px; top: 0; width: 219px; height: 198px; background: var(--navy); }
  .card__band { position: absolute; left: 0; bottom: 0; width: 399px; height: 50px; }
  .card__web { position: absolute; left: 0; bottom: 9px; width: 399px; text-align: center; color: #fff; font-size: 8px; font-weight: 600; letter-spacing: 2.6px; }
  .card--front .brand { left: 90px; top: 40px; width: 219px; flex-direction: column; gap: 12px; }
  .card--front .brand__dot { width: 70px; height: 70px; }
  .card--front .brand__name { font-size: 19px; line-height: 1.2; width: 180px; white-space: normal; text-align: center; }

  .card__ghost { position: absolute; left: 20px; top: 36px; width: 160px; height: 160px; border-radius: 50%; border: 12px solid var(--faint); }
  .holder { position: absolute; left: 52px; top: 100px; text-align: center; }
  .holder__name { font-size: 16px; font-weight: 600; color: var(--navy); }
  .holder__role { font-size: 8px; letter-spacing: 3px; color: var(--grey); }
  .card-contacts { position: absolute; left: 218px; top: 58px; list-style: none; color: var(--ink); font-size: 7.4px; font-weight: 600; }
  .card-contacts li { display: flex; align-items: flex-start; gap: 10px; margin-bottom: 12px; line-height: 9.5px; }
  .card-contacts svg { width: 11px; height: 11px; flex: none; margin-top: 1px; }
</style>
</head>
<body>
<main class="stage">

  <article class="letterhead">
    <svg class="letterhead__header" viewBox="0 0 589 150" preserveAspectRatio="none">
      <path d="M0 0H589V122Q300 120 0 145Z" fill="var(--navy)"/>
    </svg>
    <div class="brand">
      <span class="brand__dot"></span>
      <span class="brand__name">HARLOW BAY CONSULTING</span>
    </div>
    <ul class="header-contacts">
      <li><svg viewBox="0 0 10 10"><path d="M2 1L4 3L3 4Q4 6 6 7L7 6L9 8L8 9Q3 9 1 2Z" fill="#fff"/></svg>+00 1234 555 0100</li>
      <li><svg viewBox="0 0 10 10"><rect x="1" y="2" width="8" height="6" fill="none" stroke="#fff"/><path d="M1 2L5 5L9 2" fill="none" stroke="#fff"/></svg>harlowbay@mail.com</li>
      <li><svg viewBox="0 0 10 10"><circle cx="5" cy="5" r="4" fill="none" stroke="#fff"/><path d="M1 5H9M5 1V9" stroke="#fff"/></svg>harlowbayconsulting.com</li>
      <li><svg viewBox="0 0 10 10"><path d="M5 9L2 5A3 3 0 1 1 8 5Z" fill="#fff"/></svg><span>Street, 12 Sample Road,<br>Fairview, Oregon, 00900</span></li>
    </ul>

    <h1 class="subject">SUBJECT HERE</h1>
    <p class="date">Tuesday, 02/02/2020</p>
    <div class="letter-body">
      <p>Lorem ipsum dolor sit amet, consectetur adipisicing elit, sed do eiusmod tempor incididunt ut abore et dolore magna aliqua. Ut enim ad minim veniam,quis nostr exercitation ullamco laborisnisi ut aliquip ex ea commodoconsequat. Duis aute irure dolor in reprehenderit in voluptate velit essecillum dolore eu fugiat nulla pariatur. Excepteur sint occaecat cupidatat non proident, sunt in culpa qui officia deserunt mollit anim id est laborum. Lorem ipsum dolor sit amet, consectetur ire dolor in reprehenderit in volu ipsum.</p>
      <p>Minim veniam,quis nostr exercitation ullamco laborisnisi ut aliquip ex ea commo doconsequat. Duis aute irure dolor in reprehenderit in voluptate velit essecillum dolore eu fugiat nulla pariatur. Excepteur sint occaecat cupidatat non proident, sunt in culpa qui officia deserunt mollit anim id est laborum.</p>
      <p>Minim veniam,quis nostr exercitation ullamco laborisnisi ut aliquip ex ea commo doconsequat. Duis aute irure dolor in reprehenderit in voluptate velit.</p>
      <p>Minim veniam,quis nostr exercitation ullamco laborisnisi ut aliquip ex ea commo doconsequat. Duis aute irure dolor in reprehenderit in voluptate velit essecillum dolore eu fugiat nulla pariatur. Excepteur sint occaecat cupidatat non proident, sunt in culpa qui officia deserunt mollit anim id est laborum.</p>
    </div>
    <div class="signature" role="img" aria-label="Handwritten signature"></div>
    <div class="signatory">
      <p class="signatory__name">Daniel Price</p>
      <p class="signatory__role">Product Director</p>
    </div>

    <svg class="letterhead__footer" viewBox="0 0 589 60" preserveAspectRatio="none">
      <path d="M0 34Q320 32 589 8V60H0Z" fill="var(--blue)"/>
    </svg>
  </article>

  <section class="card card--front">
    <div class="card__panel"></div>
    <div class="brand">
      <span class="brand__dot"></span>
      <span class="brand__name">HARLOW BAY CONSULTING</span>
    </div>
    <svg class="card__band" viewBox="0 0 399 50" preserveAspectRatio="none">
      <path d="M0 25H260Q350 22 399 0V50H0Z" fill="var(--blue)"/>
    </svg>
    <p class="card__web">www.harlowbayconsulting.com</p>
  </section>

  <section class="card card--back">
    <div class="card__ghost"></div>
    <div class="holder">
      <p class="holder__name">YOUR NAME</p>
      <p class="holder__role">Designation</p>
    </div>
    <ul class="card-contacts">
      <li><svg viewBox="0 0 10 10"><rect x="1" y="2" width="8" height="6" fill="var(--navy)"/><path d="M1 2L5 5L9 2" fill="none" stroke="#fff" stroke-width=".8"/></svg><span>harlowbay@mail.com<br>harlowbayconsulting@domain.com</span></li>
      <li><svg viewBox="0 0 10 10"><path d="M2 1L4 3L3 4Q4 6 6 7L7 6L9 8L8 9Q3 9 1 2Z" fill="var(--navy)"/></svg><span>+00 1234 555 0100<br>+00 1234 555 0100</span></li>
      <li><svg viewBox="0 0 10 10"><path d="M5 1L10 5H8.5V9H6V6.5H4V9H1.5V5H0Z" fill="var(--navy)"/></svg><span>Street, 12 Sample Road,<br>Fairview, Oregon, 00900</span></li>
      <li><svg viewBox="0 0 10 10"><circle cx="5" cy="5" r="4.5" fill="var(--navy)"/><path d="M1 5H9M5 1V9" stroke="#fff" stroke-width=".7"/></svg>www.harlowbayconsulting.com</li>
    </ul>
  </section>

</main>
</body>
</html>
```